Personal training and nutrition business needs business card design

We need a business card that outlays our services and invites potential customers to join our team and take the first step to a healthier and more enjoyable life. We cater for any level of fitness and specialize in weight loss and conditioning, strength training, muscle gain and strength endurance. Whether you are just starting off or need some help getting to the next level of your journey we are here to get the job done.
We specialize in one on one or one on two personal training sessions and each program will be custom made to suit individual fitness goals of our clients

```html
<!DOCTYPE html>
<html lang="en">
<head>
<meta charset="utf-8">
<title>Pulse &amp; Pace – Business Card</title>
<link href="https://fonts.googleapis.com/css2?family=Roboto:ital,wght@0,400;1,400;1,500;1,700&family=Saira:ital,wght@0,800;1,700&display=swap" rel="stylesheet">
<style>
  :root {
    --purple: #7f4a9b;
    --purple-light: #9a5fba;
    --ink: #0a0a0c;
    --paper: #ffffff;
    --stage: #e8e8ea;
    --white: #ffffff;
  }
  * { margin: 0; padding: 0; box-sizing: border-box; }
  html, body { width: 1200px; height: 1000px; overflow: hidden; }
  body { background: var(--stage); position: relative; font-family: "Roboto", Arial, sans-serif; }

  .card { position: absolute; left: 317px; width: 567px; height: 325px; overflow: hidden;
          box-shadow: 5px 5px 6px rgba(0,0,0,.35); }

  /* Front */
  .card-front { top: 130px; background: var(--paper); }
  .card-front .base-band { position: absolute; left: 0; right: 0; bottom: 0; height: 29px; background: var(--purple); }
  .brand { position: absolute; text-align: center; }
  .brand-mark { display: block; margin: 0 auto 6px; width: 26px; height: 26px; border-radius: 50%; background: var(--purple-light); }
  .brand-name { font-family: "Saira", "Arial Black", sans-serif; font-weight: 800; font-size: 19px; line-height: 19px; letter-spacing: .5px; }
  .brand-tagline { font-family: "Saira", Arial, sans-serif; font-weight: 800; font-size: 5px; letter-spacing: .4px; color: var(--purple); margin-top: 4px; }
  .card-front .brand { left: 425px; top: 34px; width: 112px; }
  .card-front .brand-name { color: var(--ink); }

  .holder-name { position: absolute; left: 34px; top: 166px; color: var(--purple); font-weight: 700; font-style: italic; font-size: 22px; }
  .holder-role { position: absolute; left: 35px; top: 192px; color: var(--ink); font-style: italic; font-size: 14px; }
  .divider { position: absolute; left: 34px; top: 215px; width: 497px; height: 2px; background: var(--purple); }

  .contact { position: absolute; list-style: none; color: var(--purple); font-style: italic; font-weight: 500; font-size: 14.5px; }
  .contact li { display: flex; align-items: center; height: 22.5px; }
  .contact svg { width: 12px; height: 12px; margin-right: 7px; flex: none; }
  .contact-lines { left: 37px; top: 229px; }
  .address { position: absolute; left: 391px; top: 229px; color: var(--purple); font-style: italic; font-weight: 500; font-size: 14.5px; line-height: 22px; }
  .address svg { position: absolute; left: -17px; top: 4px; width: 11px; height: 13px; }

  /* Back */
  .card-back { top: 526px; background: var(--ink); }
  .card-back .shapes { position: absolute; inset: 0; }
  .card-back .brand { left: 70px; top: 104px; width: 118px; }
  .card-back .brand-name { color: var(--white); }

  .services { position: absolute; left: 277px; top: 64px; list-style: none; color: var(--white);
              font-family: "Saira", Arial, sans-serif; font-style: italic; font-weight: 700; font-size: 15px; letter-spacing: 1px; line-height: 30px; text-transform: uppercase; }
  .services li { position: relative; padding-left: 16px; }
  .services li::before { content: ">"; position: absolute; left: 0; font-style: normal; }
  .services .wrap { line-height: 24px; }
  .motto { position: absolute; left: 0; right: 0; top: 296px; text-align: center; color: var(--white);
           font-family: "Saira", Arial, sans-serif; font-style: italic; font-weight: 700; font-size: 10px; letter-spacing: 9px; }
</style>
</head>
<body>

<section class="card card-front">
  <div class="brand">
    <span class="brand-mark"></span>
    <div class="brand-name">PULSE<br>&amp; PACE</div>
    <div class="brand-tagline">PERSONAL TRAINING. NUTRITION. MOTIVATION</div>
  </div>

  <h1 class="holder-name">YOUR NAME</h1>
  <p class="holder-role">Founder</p>
  <div class="divider"></div>

  <ul class="contact contact-lines">
    <li><svg viewBox="0 0 24 24"><path fill="#0a0a0c" d="M6.6 10.8a15 15 0 0 0 6.6 6.6l2.2-2.2a1 1 0 0 1 1-.25 11.4 11.4 0 0 0 3.6.57 1 1 0 0 1 1 1V20a1 1 0 0 1-1 1A17 17 0 0 1 3 4a1 1 0 0 1 1-1h3.5a1 1 0 0 1 1 1c0 1.25.2 2.45.57 3.57a1 1 0 0 1-.25 1z"/></svg>020 3000 4187</li>
    <li><svg viewBox="0 0 24 24"><rect x="6" y="1.5" width="12" height="21" rx="2" fill="none" stroke="#0a0a0c" stroke-width="2"/><circle cx="12" cy="19" r="1.2" fill="#0a0a0c"/></svg>07700900316</li>
    <li><svg viewBox="0 0 24 24" fill="none" stroke="#0a0a0c" stroke-width="2"><circle cx="12" cy="12" r="10"/><path d="M2 12h20M12 2c3 3 3 17 0 20M12 2c-3 3-3 17 0 20"/></svg>website-name.com</li>
  </ul>

  <address class="address">
    <svg viewBox="0 0 20 24"><path fill="#0a0a0c" d="M10 0a8 8 0 0 0-8 8c0 6 8 16 8 16s8-10 8-16a8 8 0 0 0-8-8zm0 11a3 3 0 1 1 0-6 3 3 0 0 1 0 6z"/></svg>
    Marlow Avenue<br>Brookfield, Essex<br>CM00 4QT
  </address>

  <div class="base-band"></div>
</section>

<section class="card card-back">
  <svg class="shapes" width="567" height="325" viewBox="0 0 567 325">
    <path fill="#7f4a9b" d="M383 0H567V325H340a30 30 0 0 1-32-34L348 30A36 36 0 0 1 383 0Z"/>
    <rect x="270" y="125" width="90" height="16" rx="8" fill="#7f4a9b"/>
    <rect x="239" y="209" width="110" height="16" rx="8" fill="#7f4a9b"/>
    <rect x="300" y="110" width="140" height="15" rx="7.5" fill="#0a0a0c"/>
    <rect x="300" y="141" width="140" height="15" rx="7.5" fill="#0a0a0c"/>
    <rect x="300" y="225" width="111" height="15" rx="7.5" fill="#0a0a0c"/>
  </svg>

  <div class="brand">
    <span class="brand-mark"></span>
    <div class="brand-name">PULSE<br>&amp; PACE</div>
    <div class="brand-tagline">PERSONAL TRAINING. NUTRITION. MOTIVATION</div>
  </div>

  <ul class="services">
    <li>Weight loss</li>
    <li>Strength training</li>
    <li>Muscle gain</li>
    <li>Strength endurance</li>
    <li class="wrap">Customised personal<br>training sessions</li>
  </ul>

  <p class="motto">"STRONG BODY STRONG MIND"</p>
</section>

</body>
</html>
```